Luxury Home Brochure

Hello, I need a luxury home brochure. 11x17 double side I will need source files. see example is ok to use. Make it better. See attached here is link to downloadable editable files. Use the same pictures and words please. Thank you

https://parcelvoom.net/downloads/a41bc7e2290d385fe7a1c94b0d6e77f510490327185536/7f2d8ea90c41b65e3a09d17c2f88e01a10490327185536/k7319q

```html
<!DOCTYPE html>
<html lang="en">
<head>
<meta charset="UTF-8">
<title>Luxury Home Brochure – 4120 Quiet Canyon Rd</title>
<link href="https://fonts.googleapis.com/css2?family=Great+Vibes&family=Arimo:wght@400;700&display=swap" rel="stylesheet">
<style>
  :root{
    --page-bg:#ffffff;
    --panel-left:#f3f3f3;
    --panel-center:#e9e9e9;
    --panel-right:#cbcbcb;
    --bar:#2a2a2a;
    --bar-text:#ffffff;
    --ink:#1c1c1c;
    --rule:#2a2a2a;
    --photo-shadow:rgba(0,0,0,.45);
  }
  *{box-sizing:border-box;margin:0;padding:0}
  html,body{width:1200px;height:848px;overflow:hidden;background:var(--page-bg)}
  body{font-family:"Arimo",Arial,sans-serif;color:var(--ink)}

  .brochure{
    position:absolute;left:30px;top:30px;width:1140px;height:788px;
    display:flex;box-shadow:0 4px 18px rgba(0,0,0,.18);
  }
  .panel{position:relative;height:100%;display:flex;flex-direction:column}
  .panel--features{width:320px;background:var(--panel-left);padding:58px 14px 40px 20px}
  .panel--overview{width:500px;background:var(--panel-center);padding:32px 58px 30px 58px}
  .panel--amenities{width:320px;background:var(--panel-right);padding:58px 24px 40px 20px}

  .script-bar{
    background:var(--bar);color:var(--bar-text);
    font-family:"Great Vibes",cursive;font-size:30px;line-height:1;
    height:50px;display:flex;align-items:center;justify-content:center;
  }
  .script-bar--address{height:42px;font-size:27px;margin:4px 0 6px}

  .photo{
    border-radius:14px;box-shadow:4px 5px 8px var(--photo-shadow);
    border:2px solid #fff;
  }

  /* Features panel */
  .features-copy{margin-top:22px;font-size:11.5px;line-height:1.35}
  .features-copy p{margin-bottom:16px}
  .features-photos{margin-top:auto;display:flex;flex-direction:column;gap:16px}
  .features-photos .photo{height:164px}
  .photo--entry{background:linear-gradient(160deg,#8fb7d4 0%,#e9ece9 35%,#c9c2b4 65%,#6d6a5f 100%)}
  .photo--living-sky{background:linear-gradient(180deg,#8aa6c0 0%,#e6dccb 45%,#b7a58c 75%,#6b5b48 100%)}
  .script-bar--views{margin-top:12px;height:44px}

  /* Overview panel */
  .photo--exterior-dusk{height:196px;background:linear-gradient(180deg,#2f5a8f 0%,#6c86a8 35%,#d7a86b 60%,#3c3a30 85%,#2b3a22 100%)}
  .photo-grid{display:grid;grid-template-columns:1fr 1fr;gap:12px 22px}
  .photo-grid .photo{height:132px}
  .photo--pool-evening{background:linear-gradient(180deg,#33547e 0%,#b69a72 45%,#2f86c4 70%,#1e5f95 100%)}
  .photo--patio-night{background:linear-gradient(180deg,#1f3350 0%,#c79a5a 45%,#7b6a55 70%,#2c4e80 100%)}
  .photo--indoor-pool{background:linear-gradient(180deg,#c9d8e4 0%,#e3d8c7 40%,#8f8a84 65%,#b8a58a 100%)}
  .photo--great-room{background:linear-gradient(180deg,#a9c2da 0%,#eee6d8 40%,#a99276 70%,#7a6a5a 100%)}

  .spec-strip{
    margin-top:14px;background:var(--bar);color:var(--bar-text);
    height:76px;display:flex;justify-content:space-around;align-items:center;padding:0 18px;
  }
  .spec{display:flex;flex-direction:column;align-items:center;gap:5px;font-size:11px;letter-spacing:.2px}
  .spec svg{width:46px;height:38px;stroke:#fff;fill:none;stroke-width:2}
  .overview-copy{
    margin-top:12px;border-left:2px solid var(--rule);padding-left:6px;
    font-size:12.5px;line-height:1.55;
  }

  /* Amenities panel */
  .amenity-grid{margin-top:16px;display:grid;grid-template-columns:1fr 1fr;gap:10px 8px}
  .amenity-grid .photo{height:82px;border-radius:12px}
  .photo--kitchen{background:linear-gradient(180deg,#d9d3c6 0%,#b89c76 50%,#6f5a44 100%)}
  .photo--kitchen-island{background:linear-gradient(180deg,#e4ddd0 0%,#c9a55c 50%,#6b5946 100%)}
  .photo--closet{background:linear-gradient(180deg,#d7c6a8 0%,#efe7da 50%,#a68b68 100%)}
  .photo--pool-spa{background:linear-gradient(180deg,#7fb0d9 0%,#5c8a54 40%,#3aa0c8 70%,#c9b59a 100%)}
  .photo--master-bath{margin-top:12px;height:172px;background:linear-gradient(180deg,#a9c3d8 0%,#e4dccf 40%,#c7ad8a 70%,#8c7358 100%)}
  .amenities-copy{
    margin-top:38px;border-left:2px solid var(--rule);padding-left:7px;
    font-size:11.5px;line-height:1.45;text-align:justify;
  }
  .script-bar--more{margin-top:auto;height:44px}
</style>
</head>
<body>
<main class="brochure">

  <section class="panel panel--features">
    <h2 class="script-bar">Features</h2>
    <div class="features-copy">
      <p>Visit this stunning home with floor-to-ceiling glass windows to a beautiful view!</p>
      <p>This home has &nbsp;4 bedrooms, 3.5 bathrooms, and a 4-car garage.</p>
      <p>The master suite has a fireplace, sitting area, and a large walk-in closet. This home is perfect for entertaining!</p>
      <p>The heated floors are solar-powered with 2 Voltaris backup batteries.</p>
    </div>
    <div class="features-photos">
      <div class="photo photo--entry" role="img" aria-label="Photo of the covered front entry with glass doors and landscaping"></div>
      <div class="photo photo--living-sky" role="img" aria-label="Photo of the living room with sky-painted ceiling and garden view"></div>
    </div>
    <h2 class="script-bar script-bar--views">Veiws</h2>
  </section>

  <section class="panel panel--overview">
    <div class="photo photo--exterior-dusk" role="img" aria-label="Photo of the home exterior at dusk with palm trees and lit windows"></div>
    <h1 class="script-bar script-bar--address">4120 Quiet Canyon Rd</h1>
    <div class="photo-grid">
      <div class="photo photo--pool-evening" role="img" aria-label="Photo of the pool and home in the evening"></div>
      <div class="photo photo--patio-night" role="img" aria-label="Photo of the lit patio and pool at night"></div>
      <div class="photo photo--indoor-pool" role="img" aria-label="Photo of the sunroom looking onto the pool"></div>
      <div class="photo photo--great-room" role="img" aria-label="Photo of the great room with piano and fireplace"></div>
    </div>

    <div class="spec-strip">
      <div class="spec">
        <svg viewBox="0 0 46 38" aria-hidden="true"><rect x="5" y="6" width="36" height="16" rx="2"/><rect x="10" y="11" width="11" height="7" rx="2"/><rect x="25" y="11" width="11" height="7" rx="2"/><path d="M3 22h40v9H3zM6 31v4M40 31v4"/></svg>
        <span>3 BED</span>
      </div>
      <div class="spec">
        <svg viewBox="0 0 46 38" aria-hidden="true"><path d="M10 19V7a4 4 0 0 1 8 0"/><path d="M4 19h38v5a9 9 0 0 1-9 9H13a9 9 0 0 1-9-9z"/><path d="M11 33l-2 4M35 33l2 4"/></svg>
        <span>2.5 BATH</span>
      </div>
      <div class="spec">
        <svg viewBox="0 0 46 38" aria-hidden="true"><rect x="6" y="2" width="34" height="34"/><path d="M6 16h14M20 2v10M20 20v16M26 16h14M28 16v20M6 26h8"/></svg>
        <span>3,965SQFT</span>
      </div>
      <div class="spec">
        <svg viewBox="0 0 46 38" aria-hidden="true"><path d="M2 36h42M8 36l4-12h22l4 12M15 24l-2 12M20 24v12M26 24v12M31 24l2 12"/><path d="M37 22l-5-8h3l-4-6h2l-3-6-3 6h2l-4 6h3l-5 8z" transform="translate(6 0)"/></svg>
        <span>14.6 ACRE LOT</span>
      </div>
    </div>

    <p class="overview-copy">The solar-powered pool and spa are perfect for &nbsp;relaxing after a long day. There are 9 indoor and outdoor security cameras to keep your family safe. The master bath has a soaking tub with jets and a stunning view. The property also includes an orchard with oranges, lemons, berries, grapefruit, and a vegetable garden.</p>
  </section>

  <section class="panel panel--amenities">
    <h2 class="script-bar">Amenities</h2>
    <div class="amenity-grid">
      <div class="photo photo--kitchen" role="img" aria-label="Photo of the kitchen with breakfast bar"></div>
      <div class="photo photo--kitchen-island" role="img" aria-label="Photo of the kitchen island and dining area"></div>
      <div class="photo photo--closet" role="img" aria-label="Photo of the walk-in closet with built-in shelving"></div>
      <div class="photo photo--pool-spa" role="img" aria-label="Photo of the pool and spa in the garden"></div>
    </div>
    <div class="photo photo--master-bath" role="img" aria-label="Photo of the master bath with soaking tub, fireplace and garden view"></div>
    <p class="amenities-copy">The master bedroom has a safe and a coffee bar. There is also a large his and her side closet. All of the doors and windows are custom made in Italy. This is a once in a lifetime opportunity! Don't miss your chance to own this piece of paradise!</p>
    <h2 class="script-bar script-bar--more">And More....</h2>
  </section>

</main>
</body>
</html>
```